Pale Harbor - post rock band album cover design

We are Pale Harbor, a post-rock band based on San Jose, CA, USA. We will release a new album “Where the rivers fold" and need a album cover.

The new album is full of emotion and energy. song list:
1. Forward
2. Search (in uploaded files)
3. Before
4. Memory
5. Dream
6. Spring
7. Om Namah Shivaya

Please hear our previous music here
https://pale-harbor.tunecrate-demo.net/album/pale-harbor

Target Market(s)

music lovers

Industry/Entity Type

Music Download

Colors

Requirements
Must have
• album cover + back
• For cover we only need band name (do not need album name), want to use some streamline font for the band name "Pale Harbor"
• I attached an example from another band
Nice to have
• I don't want to limit the designers, so please listen to the music and design what you feel the best:)

```html
<!DOCTYPE html>
<html lang="en">
<head>
<meta charset="utf-8">
<title>Pale Harbor – Where the rivers fold</title>
<link rel="stylesheet" href="https://fonts.googleapis.com/css2?family=Italianno&display=swap">
<style>
  :root {
    --page-bg: #ffffff;
    --panel-edge: #2a2a33;
    --haze-deep: #1b1826;
    --haze-mid: #2e3344;
    --haze-light: #6d7d8e;
    --haze-violet: #3a2f48;
    --ink-light: #f4f4f6;
  }
  * { margin: 0; padding: 0; box-sizing: border-box; }
  html, body {
    width: 1200px;
    height: 1200px;
    overflow: hidden;
    background: var(--page-bg);
  }
  .sleeve {
    position: relative;
    width: 1200px;
    height: 1200px;
  }
  .sleeve-panel {
    position: absolute;
    top: 301px;
    width: 558px;
    height: 559px;
    border: 1px solid var(--panel-edge);
    overflow: hidden;
    color: var(--ink-light);
    font-family: "Italianno", cursive;
  }
  .sleeve-panel--front { left: 34px; }
  .sleeve-panel--back { left: 608px; }
  .stage-haze {
    position: absolute;
    inset: 0;
    background:
      radial-gradient(ellipse 45% 30% at 30% 22%, rgba(109,125,142,0.55), transparent 70%),
      radial-gradient(ellipse 40% 35% at 72% 30%, rgba(109,125,142,0.4), transparent 70%),
      radial-gradient(ellipse 60% 40% at 50% 55%, rgba(58,47,72,0.6), transparent 75%),
      linear-gradient(180deg, var(--haze-mid) 0%, var(--haze-deep) 70%, #141220 100%);
  }
  .band-name {
    position: absolute;
    left: 0;
    right: 0;
    top: 232px;
    text-align: center;
    font-size: 104px;
    line-height: 1;
    font-weight: 400;
  }
  .album-title {
    position: absolute;
    left: 36px;
    top: 42px;
    font-size: 52px;
    line-height: 1;
    font-weight: 400;
  }
  .track-list {
    position: absolute;
    left: 46px;
    top: 140px;
    list-style: none;
    font-size: 38px;
    line-height: 56px;
  }
</style>
</head>
<body>
  <main class="sleeve">
    <section class="sleeve-panel sleeve-panel--front">
      <div class="stage-haze" role="img" aria-label="Photograph of stage lights shining through dark blue smoke"></div>
      <h1 class="band-name">Pale Harbor</h1>
    </section>
    <section class="sleeve-panel sleeve-panel--back">
      <div class="stage-haze" role="img" aria-label="Photograph of stage light beams in dark blue haze"></div>
      <h2 class="album-title">Where the rivers fold</h2>
      <ol class="track-list">
        <li>1. Forward</li>
        <li>2. Search</li>
        <li>3. Before</li>
        <li>4. Memory</li>
        <li>5. Dream</li>
        <li>6. Spring</li>
        <li>7. Om Namah Shivaya</li>
      </ol>
    </section>
  </main>
</body>
</html>
```